Harbor Vitality Chocolate Shake Label

We need a new label design for our Harbor Vitality Chocolate Protein Shake. The design needs to include all the composition info as per the attached Trim Meadow Chocolate shake label with a fresh new eye catching design that will stand out on retail store shelves. It must include our Harbor Vitality Logo and portray a professional image that inspires trust. It must indicate that it is a chocolate shake that looks tasty and inviting. Harbor Vitality is a product sold by healthcare practitioners.

Industry/Entity Type

Health And Wellness

Requirements
Must have
• The Harbor Vitality logo. Contain all the attached info as per the chocolate Trim Meadow label. Feature something that indicates it is a chocolate shake on the label that looks tasty and inviting.
Nice to have
• I have attached some of the other products in our range. Would be a bonus if it can match into the existing look and feel somehow.

```html
<!DOCTYPE html>
<html lang="en">
<head>
<meta charset="utf-8">
<title>Harbor Vitality Chocolate Protein Shake Label</title>
<link href="https://fonts.googleapis.com/css2?family=Kaushan+Script&family=Nunito:ital,wght@0,700;0,900;1,900&family=Roboto+Condensed:wght@400;700&family=Montserrat:wght@700&display=swap" rel="stylesheet">
<style>
  :root {
    --brown-dark: #3d2216;
    --brown-choc: #6b2e12;
    --choc-light: #7a4228;
    --choc-deep: #3f2012;
    --orange-top: #9c4f1f;
    --orange-mid: #c97424;
    --orange-low: #f0a028;
    --gold: #f3a233;
    --blue: #1e7fc1;
    --ink: #2b1a12;
    --paper: #ffffff;
  }
  * { box-sizing: border-box; margin: 0; padding: 0; }
  html, body { width: 1200px; height: 1200px; overflow: hidden; background: var(--paper); }
  .canvas { position: relative; width: 1200px; height: 1200px; }

  .label { position: absolute; left: 82px; width: 1030px; height: 295px; font-family: "Roboto Condensed", sans-serif; color: var(--ink); overflow: hidden; }
  .label--amber { top: 282px; background: linear-gradient(180deg, var(--orange-top) 0%, var(--orange-mid) 45%, var(--orange-low) 100%); }
  .label--white { top: 622px; background: var(--paper); }

  .band { position: absolute; left: 0; width: 100%; background: var(--brown-dark); }
  .band--top { top: 0; height: 31px; }
  .band--bottom { bottom: 0; height: 37px; display: flex; align-items: center; justify-content: center; }
  .band-title { font-family: "Montserrat", sans-serif; font-weight: 700; font-size: 18px; letter-spacing: 3px; color: var(--gold); }

  .nutrition { position: absolute; left: 58px; top: 6px; width: 118px; height: 283px; background: var(--paper); border: 1.5px solid #000; padding: 2px 4px; font-size: 5.4px; line-height: 6.85px; color: #000; z-index: 2; }
  .nutrition h3 { font-size: 11px; line-height: 12px; font-weight: 700; border-bottom: 1px solid #000; }
  .nutrition .meta { border-bottom: 2px solid #000; }
  .nutrition .head { font-weight: 700; border-bottom: 1px solid #000; }
  .nutrition .row { display: flex; justify-content: space-between; border-bottom: 0.5px solid #bbb; }

  .ingredients { position: absolute; left: 190px; top: 125px; width: 180px; font-size: 6.6px; line-height: 9px; }
  .ingredients h4 { font-size: 8.5px; font-weight: 700; margin-bottom: 1px; }
  .ingredients .allergens { font-weight: 700; margin-top: 5px; }

  .brand-badge { position: absolute; left: 416px; top: 48px; width: 174px; height: 72px; border-radius: 50%; background: var(--paper); border: 4px solid var(--brown-choc); display: flex; align-items: center; justify-content: center; }
  .brand-name { font-family: "Nunito", sans-serif; font-weight: 900; font-size: 19px; color: var(--blue); white-space: nowrap; }
  .brand-plain { position: absolute; left: 416px; top: 58px; width: 190px; text-align: center; }
  .brand-plain .brand-name { font-size: 24px; }

  .product-title { position: absolute; text-align: center; z-index: 2; }
  .flavour { font-family: "Kaushan Script", cursive; font-size: 66px; line-height: 72px; color: var(--brown-choc); white-space: nowrap; }
  .product-type { font-family: "Nunito", sans-serif; font-weight: 900; font-style: italic; font-size: 31px; line-height: 34px; color: var(--brown-dark); margin-top: -6px; }
  .net-weight { font-family: "Nunito", sans-serif; font-weight: 700; font-size: 16px; color: var(--ink); margin-top: 2px; }
  .label--amber .product-title { left: 385px; top: 120px; width: 270px; }
  .label--white .product-title { left: 372px; top: 118px; width: 270px; }

  .chocolate-art { position: absolute; border-radius: 18px; background: linear-gradient(135deg, var(--choc-light) 0%, var(--choc-deep) 100%); z-index: 1; }
  .label--amber .chocolate-art { left: 672px; top: 96px; width: 168px; height: 140px; }
  .label--white .chocolate-art { left: 650px; top: 42px; width: 190px; height: 210px; }

  .servings { position: absolute; text-align: center; color: var(--gold); font-family: "Nunito", sans-serif; font-weight: 900; z-index: 2; }
  .servings .count { font-size: 34px; line-height: 32px; display: block; }
  .servings .unit { font-size: 13px; line-height: 13px; color: #fff; }
  .label--amber .servings { left: 712px; top: 172px; width: 60px; }
  .label--white .servings { left: 712px; top: 190px; width: 60px; }

  .free-from { position: absolute; left: 690px; top: 44px; width: 140px; font-size: 7.4px; line-height: 10px; font-weight: 700; color: #fff; }

  .info { position: absolute; left: 853px; top: 58px; width: 165px; font-size: 6.6px; line-height: 9px; z-index: 2; }
  .info h4 { font-size: 8.5px; font-weight: 700; margin-bottom: 1px; }
  .info p { margin-bottom: 6px; }
  .info .strong { font-weight: 700; }
  .info .field { font-size: 8.5px; font-weight: 700; margin-bottom: 10px; }
</style>
</head>
<body>
<main class="canvas">

  <section class="label label--amber">
    <div class="band band--top"></div>
    <div class="band band--bottom"><span class="band-title">DIETARY SUPPLEMENT</span></div>

    <div class="nutrition">
      <h3>Nutrition Facts</h3>
      <div class="meta">Serving Size 50ml (2x25ml)<br>Servings per 900g container: ±28 days</div>
      <div class="head">Amount per serving of 30g</div>
      <div class="row"><span>Protein</span><span>7 g</span></div>
      <div class="row"><span>Carbohydrates</span><span>16 g</span></div>
      <div class="row"><span>Fibre</span><span>2.5 g</span></div>
      <div class="row"><span>Fat</span><span>1 g</span></div>
      <div class="row"><span>Energy</span><span>348 kJ</span></div>
      <div class="row"><span>Sodium</span><span>106 mg</span></div>
      <div class="row"><span>Potassium</span><span>155 mg</span></div>
      <div class="row"><span>Calcium</span><span>203 mg</span></div>
      <div class="row"><span>Magnesium</span><span>46 mg</span></div>
      <div class="row"><span>Phosphorous</span><span>174 mg</span></div>
      <div class="row"><span>L-Glutamine</span><span>100 mg</span></div>
      <div class="row"><span>Choline</span><span>30 mg</span></div>
      <div class="row"><span>Pyruvite</span><span>21.8 mg</span></div>
      <div class="row"><span>L-Carnitine</span><span>15 mg</span></div>
      <div class="row"><span>Zinc</span><span>4.5mg</span></div>
      <div class="row"><span>Molybdenum</span><span>28.5 mcg</span></div>
      <div class="row"><span>Selenium</span><span>15 mcg</span></div>
      <div class="head">Vitamins Blend Based on 30% of RDA</div>
      <div class="row"><span>Vitamin C</span><span>1.8 mg</span></div>
      <div class="row"><span>Nicotinamide</span><span>5.5 mg</span></div>
      <div class="row"><span>Pantothenic Acid</span><span>1.8 mg</span></div>
      <div class="row"><span>Vitamin B2</span><span>480 mcg</span></div>
      <div class="row"><span>Vitamin B6</span><span>600 mcg</span></div>
      <div class="row"><span>Vitamin B1</span><span>420 mcg</span></div>
      <div class="row"><span>Vitamin A</span><span>300 RE</span></div>
      <div class="row"><span>Folic Acid</span><span>80 mcg</span></div>
      <div class="row"><span>Biotin</span><span>24 mcg</span></div>
      <div class="row"><span>Vitamin E</span><span>3 TE</span></div>
      <div class="row"><span>Vitamin D</span><span>1.5 mcg</span></div>
      <div class="row"><span>Vitamin B12</span><span>0.3 mcg</span></div>
    </div>

    <div class="ingredients">
      <h4>Ingredients:</h4>
      <p>Skim Milk powder, fructose, maltodextrin, soy protein isolate, fructooligosaccharides, whey protein concentrate, calcium caseinate, instant starch, MCT oil, flavourants, calcium phosphate, stabilizers, l-glutamine, calcium pyruvate, selenium a.a.c salt, potassium phosphate, magnesium oxide, vitamin premix, garcinia cambogia extract, choline bitartrate, inositol, zinc lactate, l-carnitine, molybdneium a.a.c, sucralose sweetener blend, colourants, manganese lactate, chromium picolinate.</p>
      <p class="allergens">Allergenes: Made in a factory that processes cow's milk, egg, soy, gluten (wheat, barley and oats), fish, tree nuts and peanuts.</p>
    </div>

    <div class="brand-badge"><span class="brand-name">Harbor Vitality</span></div>

    <div class="chocolate-art" role="img" aria-label="Chocolate bar with a splash of melted chocolate"></div>

    <div class="product-title">
      <div class="flavour">Chocolate</div>
      <div class="product-type">Protein Shake</div>
      <div class="net-weight">Net Wt. 450g</div>
    </div>

    <div class="servings"><span class="count">28</span><span class="unit">serving</span></div>

    <p class="free-from">Free from trans fats, sucrose, aspartame, effedra, caffeine, artificial stimulants, wheat, gluten, yeast, corn and preservatives.</p>

    <div class="info">
      <h4>Container info:</h4>
      <p>As a dietary supplement, use to replace one protein meal per day. Blend two 25ml level scoopfuls with a full glass of water or skim milk in a shaker/blender.</p>
      <h4>Keep out of reach of children.</h4>
      <p>Store in a cool dry place. Do not use if the tamper evident seal is missing or broken.</p>
      <p class="strong">Consult with your physician before using this product if you are pregnant, lactating or suspect you may be sensitive to any of the ingredients.</p>
      <div class="field">Manufactured in:</div>
      <div class="field">Distributed by:</div>
    </div>
  </section>

  <section class="label label--white">
    <div class="band band--top"></div>
    <div class="band band--bottom"><span class="band-title">DIETARY SUPPLEMENT</span></div>

    <div class="nutrition">
      <h3>Nutrition Facts</h3>
      <div class="meta">Serving Size 50ml (2x25ml)<br>Servings per 900g container: ±28 days</div>
      <div class="head">Amount per serving of 30g</div>
      <div class="row"><span>Protein</span><span>7 g</span></div>
      <div class="row"><span>Carbohydrates</span><span>16 g</span></div>
      <div class="row"><span>Fibre</span><span>2.5 g</span></div>
      <div class="row"><span>Fat</span><span>1 g</span></div>
      <div class="row"><span>Energy</span><span>348 kJ</span></div>
      <div class="row"><span>Sodium</span><span>106 mg</span></div>
      <div class="row"><span>Potassium</span><span>155 mg</span></div>
      <div class="row"><span>Calcium</span><span>203 mg</span></div>
      <div class="row"><span>Magnesium</span><span>46 mg</span></div>
      <div class="row"><span>Phosphorous</span><span>174 mg</span></div>
      <div class="row"><span>L-Glutamine</span><span>100 mg</span></div>
      <div class="row"><span>Choline</span><span>30 mg</span></div>
      <div class="row"><span>Pyruvite</span><span>21.8 mg</span></div>
      <div class="row"><span>L-Carnitine</span><span>15 mg</span></div>
      <div class="row"><span>Zinc</span><span>4.5mg</span></div>
      <div class="row"><span>Molybdenum</span><span>28.5 mcg</span></div>
      <div class="row"><span>Selenium</span><span>15 mcg</span></div>
      <div class="head">Vitamins Blend Based on 30% of RDA</div>
      <div class="row"><span>Vitamin C</span><span>1.8 mg</span></div>
      <div class="row"><span>Nicotinamide</span><span>5.5 mg</span></div>
      <div class="row"><span>Pantothenic Acid</span><span>1.8 mg</span></div>
      <div class="row"><span>Vitamin B2</span><span>480 mcg</span></div>
      <div class="row"><span>Vitamin B6</span><span>600 mcg</span></div>
      <div class="row"><span>Vitamin B1</span><span>420 mcg</span></div>
      <div class="row"><span>Vitamin A</span><span>300 RE</span></div>
      <div class="row"><span>Folic Acid</span><span>80 mcg</span></div>
      <div class="row"><span>Biotin</span><span>24 mcg</span></div>
      <div class="row"><span>Vitamin E</span><span>3 TE</span></div>
      <div class="row"><span>Vitamin D</span><span>1.5 mcg</span></div>
      <div class="row"><span>Vitamin B12</span><span>0.3 mcg</span></div>
    </div>

    <div class="ingredients">
      <h4>Ingredients:</h4>
      <p>Skim Milk powder, fructose, maltodextrin, soy protein isolate, fructooligosaccharides, whey protein concentrate, calcium caseinate, instant starch, MCT oil, flavourants, calcium phosphate, stabilizers, l-glutamine, calcium pyruvate, selenium a.a.c salt, potassium phosphate, magnesium oxide, vitamin premix, garcinia cambogia extract, choline bitartrate, inositol, zinc lactate, l-carnitine, molybdneium a.a.c, sucralose sweetener blend, colourants, manganese lactate, chromium picolinate.</p>
      <p class="allergens">Allergenes: Made in a factory that processes cow's milk, egg, soy, gluten (wheat, barley and oats), fish, tree nuts and peanuts.</p>
    </div>

    <div class="brand-plain"><span class="brand-name">Harbor Vitality</span></div>

    <div class="chocolate-art" role="img" aria-label="Chocolate bar breaking through a splash of melted chocolate"></div>

    <div class="product-title">
      <div class="flavour">Chocolate</div>
      <div class="product-type">Protein Shake</div>
      <div class="net-weight">Net Wt. 450g</div>
    </div>

    <div class="servings"><span class="count">28</span><span class="unit">serving</span></div>

    <div class="info">
      <h4>Container info:</h4>
      <p>As a dietary supplement, use to replace one protein meal per day. Blend two 25ml level scoopfuls with a full glass of water or skim milk in a shaker/blender.</p>
      <h4>Keep out of reach of children.</h4>
      <p>Store in a cool dry place. Do not use if the tamper evident seal is missing or broken.</p>
      <p class="strong">Consult with your physician before using this product if you are pregnant, lactating or suspect you may be sensitive to any of the ingredients.</p>
      <div class="field">Manufactured in:</div>
      <div class="field">Distributed by:</div>
    </div>
  </section>

</main>
</body>
</html>
```